I am looking for a book cover designs. The title of the book is "Ways to stand out and where your habits slip"

the book is not too formal but it is also not informal.

I wish for the title to be easily readable and capturing, especially the "ways to stand out" part.

the book should also include the author name: Tobar Kessly

everyone

• Full title and author name: Tobar Kessly
• There is a chapter that is called "turn the lamp inward", if you wish to do an illustration as part of the cover then perhaps that can give you an idea of what to go with.
• anything that takes attention away from the title.Also should not include any photographs.

```html
<!DOCTYPE html>
<html lang="en">
<head>
<meta charset="UTF-8">
<title>Ways to Stand Out — Tobar Kessly</title>
<link rel="stylesheet" href="https://fonts.googleapis.com/css2?family=Bebas+Neue&family=Oswald:wght@500&display=swap">
<style>
  :root {
    --backdrop: #78797b;
    --cover-top: #e4e8ed;
    --cover-bottom: #cfd6de;
    --title-blue: #173f86;
    --subtitle-grey: #5e6063;
    --author-ink: #2a2b2d;
    --scene-light: #e9edf1;
    --scene-mid: #c3ccd5;
    --scene-shade: #9aa6b2;
  }
  * { margin: 0; padding: 0; box-sizing: border-box; }
  html, body {
    width: 1200px;
    height: 1200px;
    overflow: hidden;
    background: var(--backdrop);
  }
  .canvas {
    position: relative;
    width: 1200px;
    height: 1200px;
  }
  .book-cover {
    position: absolute;
    left: 240px;
    top: 45px;
    width: 720px;
    height: 1110px;
    background: linear-gradient(170deg, var(--cover-top) 0%, var(--cover-top) 55%, var(--cover-bottom) 100%);
    box-shadow: 0 18px 40px rgba(0,0,0,0.28);
    overflow: hidden;
  }
  .cover-title {
    position: absolute;
    left: 56px;
    top: 70px;
    font-family: "Bebas Neue", "Oswald", sans-serif;
    font-weight: 400;
    color: var(--title-blue);
    font-size: 200px;
    line-height: 0.86;
    letter-spacing: 1px;
    text-transform: uppercase;
  }
  .cover-subtitle {
    position: absolute;
    left: 58px;
    top: 432px;
    font-family: "Bebas Neue", "Oswald", sans-serif;
    color: var(--subtitle-grey);
    font-size: 84px;
    line-height: 0.92;
    text-transform: uppercase;
  }
  .cover-illustration {
    position: absolute;
    left: 0;
    top: 610px;
    width: 720px;
    height: 360px;
    background:
      radial-gradient(ellipse 200px 200px at 52% 48%, var(--scene-light) 0%, var(--scene-mid) 70%, transparent 72%),
      linear-gradient(180deg, var(--cover-top) 0%, var(--scene-mid) 100%);
  }
  .cover-author {
    position: absolute;
    left: 0;
    right: 0;
    bottom: 62px;
    text-align: center;
    font-family: "Oswald", sans-serif;
    font-weight: 500;
    font-size: 40px;
    letter-spacing: 0.5em;
    padding-left: 0.5em;
    color: var(--author-ink);
    text-transform: uppercase;
  }
</style>
</head>
<body>
  <main class="canvas">
    <article class="book-cover">
      <h1 class="cover-title">Ways to<br>stand out</h1>
      <p class="cover-subtitle">And where your<br>habits slip</p>
      <div class="cover-illustration" role="img" aria-label="A small chess pawn before a round table mirror that reflects it as a king, on a pale grey surface"></div>
      <p class="cover-author">Tobar Kessly</p>
    </article>
  </main>
</body>
</html>
```